Folded A4 flyer for design&construction company

Folded A4 flyer needed. Keywords: elegant, stylish
our website www.corvimo.ae

Industry/Entity Type

Construction

```html
<!DOCTYPE html>
<html lang="en">
<head>
<meta charset="utf-8">
<title>Corvimo – Folded A4 Flyer</title>
<link href="https://fonts.googleapis.com/css2?family=Open+Sans:wght@400;600&family=Courgette&display=swap" rel="stylesheet">
<style>
  :root {
    --backdrop: #7b7d77;
    --wall-white: #efedec;
    --wall-orange: #e3a23a;
    --floor-wood: #b8873f;
    --floor-dark: #8a6228;
    --ink: #2a2420;
    --gold: #b48a2c;
    --badge: #e7b23f;
    --text-light: #ffffff;
  }
  * { margin: 0; padding: 0; box-sizing: border-box; }
  html, body { width: 1200px; height: 789px; overflow: hidden; }
  body {
    background: var(--backdrop);
    font-family: "Open Sans", Arial, sans-serif;
    position: relative;
  }
  .spread {
    position: absolute;
    left: 105px; top: 44px;
    width: 990px; height: 700px;
    display: flex;
  }
  .page {
    position: relative;
    width: 495px; height: 700px;
    overflow: hidden;
  }
  .page-photo { position: absolute; inset: 0; }
  .back .page-photo {
    background:
      linear-gradient(180deg, rgba(239,237,236,0) 45%, rgba(184,135,63,0.9) 70%, var(--floor-dark) 100%),
      linear-gradient(100deg, var(--wall-white) 0%, #dcd8d2 45%, #e9c27a 75%, var(--wall-orange) 100%);
  }
  .front .page-photo {
    background:
      linear-gradient(180deg, rgba(0,0,0,0) 55%, rgba(184,135,63,0.95) 72%, var(--floor-dark) 100%),
      linear-gradient(90deg, var(--wall-orange) 0%, #e7b04d 40%, #f1ece6 62%, var(--wall-white) 100%);
  }
  .brand {
    position: absolute;
    display: flex; flex-direction: column; align-items: center;
    color: var(--ink);
  }
  .brand-name {
    font-weight: 600;
    letter-spacing: 2px;
    line-height: 1;
  }
  .brand-tag {
    font-family: "Courgette", cursive;
    color: var(--gold);
  }
  .back .brand { left: 195px; top: 78px; }
  .back .brand-name { font-size: 40px; }
  .back .brand-tag { font-size: 12px; }
  .about {
    position: absolute;
    left: 105px; top: 150px; width: 350px;
    font-size: 12.5px; line-height: 1.45;
    color: var(--ink);
    text-align: justify;
  }
  .contact {
    position: absolute;
    left: 160px; right: 10px; top: 470px;
    text-align: center;
    color: var(--text-light);
  }
  .contact .phone { font-size: 22px; }
  .contact .or {
    display: inline-block;
    margin: 6px 0;
    padding: 2px 10px;
    border-radius: 12px;
    background: #4a3217;
    font-size: 14px;
  }
  .contact .email { font-size: 17px; }
  .contact .address { font-size: 10.5px; margin-top: 18px; white-space: nowrap; }
  .contact .web { font-size: 15px; font-weight: 600; color: var(--ink); margin-top: 6px; }
  .quote-badge {
    position: absolute;
    left: 28px; top: 545px;
    width: 112px; height: 112px;
    border-radius: 50%;
    background: var(--badge);
    color: var(--ink);
    display: flex; flex-direction: column; align-items: center; justify-content: center;
    font-weight: 600; line-height: 1.05;
    text-transform: uppercase;
  }
  .quote-badge .small { font-size: 11px; }
  .quote-badge .big { font-size: 21px; }
  .motto {
    position: absolute;
    left: 40px; top: 42px; width: 430px;
    font-family: "Courgette", cursive;
    font-size: 16px;
    color: var(--text-light);
  }
  .motto .author { color: #6b4a14; }
  .front .brand { right: 40px; top: 240px; align-items: flex-end; }
  .front .brand-name { font-size: 58px; }
  .front .brand-tag { font-size: 14px; }
  .front .web {
    position: absolute;
    right: 40px; bottom: 70px;
    font-size: 16px; font-weight: 600;
    color: var(--ink);
  }
</style>
</head>
<body>
  <main class="spread">
    <section class="page back">
      <div class="page-photo" role="img" aria-label="Bright modern interior with white staircase, orange walls and glossy wooden floor"></div>
      <div class="brand">
        <span class="brand-name">CORVIMO</span>
        <span class="brand-tag">design &amp; construction</span>
      </div>
      <p class="about">We believe in quality beginnings and flawless finishes. We are a team of creative designers and constructors with years of experience and expertise in providing complete interior design and construction services. Our unique designing prowess is complemented by our unflinching commitment to quality construction. Our team specializes in classic and contemporary high quality construction in Dubai for commercial and residential projects.</p>
      <div class="contact">
        <div class="phone">800-CORVIMO</div>
        <div class="or">or</div>
        <div class="email">CONTACT@CORVIMO.AE</div>
        <div class="address">Corvimo LLC, Harbor Point Tower, Office 1210, Business Bay, Dubai</div>
        <div class="web">WWW.CORVIMO.AE</div>
      </div>
      <div class="quote-badge">
        <span class="small">Get a</span>
        <span class="big">Free</span>
        <span class="big">Quote</span>
        <span class="small">Today</span>
      </div>
    </section>
    <section class="page front">
      <div class="page-photo" role="img" aria-label="Modern lounge interior with orange walls, white ceiling, black chairs and wooden floor"></div>
      <p class="motto">Quality is not an act, it is a habit - <span class="author">Elias Varn</span></p>
      <div class="brand">
        <span class="brand-name">CORVIMO</span>
        <span class="brand-tag">design &amp; construction</span>
      </div>
      <div class="web">WWW.CORVIMO.AE</div>
    </section>
  </main>
</body>
</html>
```